Design an Outstanding flyer for my company.

I need a flyer designed for our window tinting company based in Brisbane Queensland Australia. The flyer will be targeting Home tinting. We also do mobile car tinting. Something in regards to this could be incorporated into the flyer as well.
I want it to be 2 sided DL size. Black background.
It really needs to Pop, and be a real attention getter.
It needs to be easy to read.
I have provided a mock up with the info on it from our marketing company. It will need a spellcheck etc to make sure everything is correct.
Everything about it can be changed however you like.
I have also included the company logo.

Lets see what you've got!

Target Market(s)

Home Owners

Industry/Entity Type

Home Improvement

Font styles to use
Other font styles liked:
• Duan Penh

Requirements
Must have
• All the information on the mock up. Clear and easy to read.
• Must Stand Out!

```html
<!DOCTYPE html>
<html lang="en">
<head>
<meta charset="utf-8">
<title>Brightline Window Tinting – DL Flyer</title>
<link rel="stylesheet" href="https://fonts.googleapis.com/css2?family=Josefin+Sans:wght@300;400;600;700&family=Roboto+Condensed:wght@700&family=Open+Sans:wght@700;800&display=swap">
<style>
  :root {
    --black: #0b0b0b;
    --charcoal: #1d1d1d;
    --yellow: #f3e51f;
    --yellow-deep: #d9c21a;
    --white: #ffffff;
    --page: #ffffff;
  }
  * { box-sizing: border-box; margin: 0; padding: 0; }
  html, body { width: 1200px; height: 1154px; overflow: hidden; background: var(--page); }
  .canvas { position: relative; width: 1200px; height: 1154px; }

  .flyer {
    position: absolute; top: 35px; width: 527px; height: 1083px;
    background: var(--black); overflow: hidden;
    font-family: "Josefin Sans", sans-serif; color: var(--white);
  }
  .flyer--front { left: 48px; }
  .flyer--back { left: 620px; }
  .flyer__art { position: absolute; inset: 0; width: 527px; height: 1083px; }

  .headline { position: absolute; left: 65px; top: 120px; line-height: 1; }
  .headline__word { display: block; font-size: 62px; letter-spacing: 3px; height: 58px; }
  .headline__word--thin { font-weight: 300; color: var(--yellow); }
  .headline__word--bold { font-weight: 700; color: var(--white); }
  .headline__sub { position: absolute; left: 65px; top: 310px; font-size: 28px; line-height: 36px; letter-spacing: 1px; }
  .headline__sub .light { font-weight: 300; color: var(--white); }
  .headline__sub .strong { font-weight: 700; color: var(--yellow); }
  .headline__sub .accent { font-weight: 400; color: var(--yellow); }

  .benefits { position: absolute; left: 0; width: 527px; top: 565px; text-align: center; font-family: "Open Sans", sans-serif; font-weight: 800; line-height: 1; }
  .benefits__line { display: block; font-size: 40px; letter-spacing: -1px; margin-bottom: 6px; }
  .benefits__line--small { font-size: 32px; }
  .hl { color: var(--yellow); }

  .reasons { position: absolute; left: 65px; top: 128px; }
  .reasons__count { font-size: 76px; font-weight: 700; color: var(--white); line-height: 1; height: 72px; }
  .reasons__line { display: block; font-size: 26px; font-weight: 600; letter-spacing: 1px; line-height: 33px; }
  .reasons__line--y { color: var(--yellow); }
  .reasons__list {
    position: absolute; left: 63px; top: 437px; width: 370px;
    font-family: "Open Sans", sans-serif; font-weight: 700; font-size: 13.4px; line-height: 22px; text-transform: uppercase;
  }

  .call-box {
    position: absolute; left: 49px; top: 685px; width: 426px; height: 193px;
    border: 2px solid var(--white); text-align: center;
    font-family: "Roboto Condensed", sans-serif; font-weight: 700;
  }
  .call-box__phone { display: block; margin-top: 8px; font-size: 66px; color: var(--yellow); line-height: 58px; letter-spacing: -1px; }
  .call-box__band { margin: 0 23px; background: var(--yellow); color: var(--black); height: 72px; padding-top: 4px; }
  .call-box__lead { display: block; font-family: "Open Sans", sans-serif; font-weight: 800; font-size: 28px; letter-spacing: -1px; line-height: 34px; }
  .call-box__lead-sub { display: block; font-family: "Open Sans", sans-serif; font-weight: 700; font-size: 16.5px; line-height: 26px; }
  .call-box__sms { display: block; margin-top: 6px; font-size: 27px; color: var(--yellow); line-height: 32px; }

  .brand { position: absolute; left: 0; width: 527px; top: 930px; display: flex; justify-content: center; align-items: center; gap: 14px; }
  .brand__dot { width: 34px; height: 34px; border-radius: 50%; background: var(--yellow); }
  .brand__name { font-size: 34px; font-weight: 700; color: var(--yellow); letter-spacing: 1px; line-height: 1; padding-top: 6px; }

  .web { position: absolute; left: 0; width: 527px; top: 1008px; text-align: center; font-size: 23px; font-weight: 600; letter-spacing: 2.4px; color: var(--yellow); }
</style>
</head>
<body>
<main class="canvas">

  <!-- Front side -->
  <section class="flyer flyer--front">
    <svg class="flyer__art" viewBox="0 0 527 1083" aria-hidden="false">
      <defs>
        <linearGradient id="frontPhoto" x1="0" y1="0" x2="1" y2="1">
          <stop offset="0" stop-color="#4a3f2c"/>
          <stop offset="0.5" stop-color="#2d2f31"/>
          <stop offset="1" stop-color="#141516"/>
        </linearGradient>
        <linearGradient id="band" x1="0" y1="0" x2="1" y2="0">
          <stop offset="0" stop-color="#0b0b0b"/>
          <stop offset="1" stop-color="#2a2a2a"/>
        </linearGradient>
      </defs>
      <g role="img" aria-label="Photo of a modern home with large tinted glass windows and hills behind">
        <polygon points="0,0 527,0 527,380 0,570" fill="url(#frontPhoto)"/>
      </g>
      <polygon points="240,640 527,480 527,700 380,700" fill="url(#band)"/>
      <polygon points="0,0 95,0 0,55" fill="var(--white)"/>
      <polygon points="18,62 120,0 310,40 62,125" fill="var(--yellow)"/>
      <polygon points="0,300 115,555 0,565" fill="var(--yellow-deep)" opacity="0.75"/>
      <polygon points="392,1083 527,985 527,1083" fill="var(--yellow)"/>
    </svg>

    <h1 class="headline">
      <span class="headline__word headline__word--thin">KEEP</span>
      <span class="headline__word headline__word--bold">HEAT</span>
      <span class="headline__word headline__word--thin">OUT</span>
    </h1>
    <p class="headline__sub">
      <span class="light">BLOCK</span><br>
      <span class="strong">99.9%</span><br>
      <span class="accent">UV RAYS</span>
    </p>

    <p class="benefits">
      <span class="benefits__line">SAVE <span class="hl">MONEY</span></span>
      <span class="benefits__line benefits__line--small"><span class="hl">INCREASE</span> PRIVACY</span>
    </p>

    <div class="call-box">
      <span class="call-box__phone">07 3100 4820</span>
      <div class="call-box__band">
        <span class="call-box__lead">CALL BRISBANE’S LEADER</span>
        <span class="call-box__lead-sub">IN HOME WINDOW TINTING NOW</span>
      </div>
      <span class="call-box__sms">SMS : 0400 582 916</span>
    </div>

    <div class="brand">
      <span class="brand__dot"></span>
      <span class="brand__name">Brightline Window Tinting</span>
    </div>
    <p class="web">www.brightlinetinting.com.au</p>
  </section>

  <!-- Back side -->
  <section class="flyer flyer--back">
    <svg class="flyer__art" viewBox="0 0 527 1083" aria-hidden="false">
      <defs>
        <linearGradient id="backPhoto" x1="0" y1="0" x2="1" y2="1">
          <stop offset="0" stop-color="#1c2a5c"/>
          <stop offset="0.5" stop-color="#1e2128"/>
          <stop offset="1" stop-color="#101112"/>
        </linearGradient>
        <linearGradient id="bandBack" x1="0" y1="0" x2="1" y2="0">
          <stop offset="0" stop-color="#0b0b0b"/>
          <stop offset="1" stop-color="#2a2a2a"/>
        </linearGradient>
      </defs>
      <g role="img" aria-label="Night photo of a home exterior with palm trees and a walkway">
        <polygon points="0,0 527,0 527,400 0,600" fill="url(#backPhoto)"/>
      </g>
      <polygon points="240,660 527,500 527,700 380,700" fill="url(#bandBack)"/>
      <polygon points="0,0 95,0 0,55" fill="var(--white)"/>
      <polygon points="18,62 120,0 315,40 62,125" fill="var(--yellow)"/>
      <polygon points="0,80 62,125 62,400 0,420" fill="var(--yellow)"/>
      <polygon points="392,1083 527,985 527,1083" fill="var(--yellow)"/>
    </svg>

    <h2 class="reasons">
      <span class="reasons__count">20</span>
      <span class="reasons__line reasons__line--y">REASONS</span>
      <span class="reasons__line">WHY</span>
      <span class="reasons__line reasons__line--y">HOME WINDOW</span>
      <span class="reasons__line">TINTING</span>
      <span class="reasons__line reasons__line--y">IS PERFECT</span>
      <span class="reasons__line">FOR YOU</span>
    </h2>
    <p class="reasons__list">Reduce glare. Reduce energy costs. Control the amount of light entering your home. Reduce carbon footprint. Make home more beautiful. Eliminate home hot spots. Protect against broken glass. Regulate energy. Protects upholstery. Improve effectiveness of roof insulation. Improve health. Reduces interior floor fading. Eliminate need for blinds. Strengthen your window</p>

    <div class="call-box">
      <span class="call-box__phone">07 3100 4820</span>
      <div class="call-box__band">
        <span class="call-box__lead">CALL BRISBANE’S LEADER</span>
        <span class="call-box__lead-sub">IN HOME WINDOW TINTING NOW</span>
      </div>
      <span class="call-box__sms">SMS : 0400 582 916</span>
    </div>

    <div class="brand">
      <span class="brand__dot"></span>
      <span class="brand__name">Brightline Window Tinting</span>
    </div>
    <p class="web">www.brightlinetinting.com.au</p>
  </section>

</main>
</body>
</html>
```